Website for The Pendry Parlour

I require a website for "The Pendry Parlour" which is a blog type business for 40+ year old women covering books, true crime, history, travel and food. It needs to support blog posts, links to social media including YouTube videos, Instagram, TikTok and Facebook. The background theme needs to be like that of a newspaper. Easy to navigate and to allow me to post blogs/videos.

```html
<!DOCTYPE html>
<html lang="en">
<head>
<meta charset="utf-8">
<title>The Pendry Parlour</title>
<link href="https://fonts.googleapis.com/css2?family=Tinos&family=Poppins:wght@300;400;500&display=swap" rel="stylesheet">
<style>
:root{
  --ink:#222;
  --dark:#2b2b2b;
  --text:#666;
  --muted:#999;
  --panel:#f3f3f3;
  --line:#e6e6e6;
  --accent:#f5a623;
  --white:#fff;
}
*{margin:0;padding:0;box-sizing:border-box}
html,body{width:1200px;height:4844px;overflow:hidden;background:var(--white)}
body{position:relative;font-family:"Poppins",sans-serif;color:var(--ink)}
.abs{position:absolute}
.serif{font-family:"Tinos",serif;font-weight:400}
.body-copy{font-size:12.5px;line-height:24px;color:var(--text);font-weight:300;text-align:justify}
.btn{position:absolute;background:var(--dark);color:var(--white);font-size:13px;display:flex;align-items:center;justify-content:center;letter-spacing:.5px}
.photo{position:absolute}

.topbar{left:0;top:0;width:1200px;height:56px;background:var(--dark)}
.topbar .links{position:absolute;left:70px;top:0;height:56px;display:flex;align-items:center;gap:44px;color:var(--white);font-size:13px}
.topbar .social{position:absolute;right:70px;top:22px;display:flex;gap:10px}
.dot{width:10px;height:10px;border-radius:50%;background:var(--white)}

.masthead{left:0;top:56px;width:1200px;height:136px;display:flex;align-items:center;justify-content:center;font-size:40px;color:var(--ink)}
.mainnav{left:0;top:192px;width:1200px;height:49px;border-top:1px solid var(--line);border-bottom:1px solid var(--line);display:flex;justify-content:center;align-items:center;gap:66px;font-size:13px;letter-spacing:.5px}

.hero{left:0;top:241px;width:1200px;height:489px;background:linear-gradient(180deg,#8fa9b7 0%,#5c7a6a 22%,#1f5e9a 40%,#2a79b4 55%,#d9c8a0 75%,#c9b48a 100%)}
.hero-box{left:527px;top:348px;width:603px;height:275px;background:rgba(255,255,255,.72);text-align:center}
.hero-box .kicker{margin-top:62px;font-size:26px}
.hero-box h1{font-size:44px;margin-top:8px;letter-spacing:.5px}
.hero-box .sub{font-size:26px;margin-top:4px}
.hero-arrow{top:458px;width:40px;height:54px;background:var(--white);display:flex;align-items:center;justify-content:center}

h2.section-title{position:absolute;font-family:"Tinos",serif;font-weight:400;font-size:40px;color:var(--ink)}
h2.center{left:0;width:1200px;text-align:center}

.card{position:absolute;background:var(--panel)}
.card .cap{position:absolute;left:0;right:0;text-align:center;font-family:"Tinos",serif;font-size:17px}

.travel-card{position:absolute;background:var(--white)}
.travel-card .meta{position:absolute;left:0;right:0;bottom:0;height:37px;background:var(--dark);color:var(--white);font-size:11px}
.travel-card .t-title{position:absolute;left:0;right:0;text-align:center;font-family:"Tinos",serif;font-size:17px}
.travel-card .t-text{position:absolute;left:20px;right:20px;text-align:center;font-size:12px;line-height:24px;color:var(--text);font-weight:300}
.guest h3{font-family:"Tinos",serif;font-weight:400;font-size:17px;margin-top:30px}
.guest p{font-size:11px;color:var(--text);line-height:20px;margin-top:6px;font-weight:300}
.guest .date{font-size:10px;font-style:italic;color:var(--muted);margin-top:10px}

.footer{left:0;top:4567px;width:1200px;height:277px;background:var(--dark);color:var(--white);text-align:center}
</style>
</head>
<body>

<header>
  <div class="abs topbar">
    <nav class="links"><span>TRUE CRIME</span><span>TRAVEL</span><span>HISTORY</span><span>BOOKS</span><span>FOOD</span></nav>
    <div class="social"><span class="dot"></span><span class="dot"></span><span class="dot"></span><span class="dot"></span></div>
  </div>
  <div class="abs masthead serif">The Pendry Parlour</div>
  <nav class="abs mainnav"><span>HOME</span><span>TRUE CRIME</span><span>TRAVEL</span><span>HISTORY</span><span>BOOKS</span><span>FOOD</span></nav>
</header>

<section>
  <div class="abs hero" role="img" aria-label="Coastal city beach with blue sea and mountains"></div>
  <div class="abs hero-box serif">
    <div class="kicker">A Guide To Inspire</div>
    <h1 class="serif">LIVING LIFE IMAGINED</h1>
    <div class="sub">A Family’s Journey from NYC to Cyprus</div>
  </div>
  <div class="abs hero-arrow" style="left:0"><svg width="12" height="20"><path d="M10 2L2 10l8 8" fill="none" stroke="#333" stroke-width="1.5"/></svg></div>
  <div class="abs hero-arrow" style="right:0"><svg width="12" height="20"><path d="M2 2l8 8-8 8" fill="none" stroke="#333" stroke-width="1.5"/></svg></div>
</section>

<section class="story">
  <div class="photo" style="left:70px;top:803px;width:504px;height:553px;background:linear-gradient(180deg,#7fb0e0 0%,#cfd7dc 35%,#7d8f6a 50%,#3f6e86 70%,#a08256 100%)" role="img" aria-label="Seaside promenade with apartment buildings and rocky shore"></div>
  <h2 class="section-title" style="left:628px;top:826px">My Story</h2>
  <div class="abs body-copy" style="left:628px;top:900px;width:504px">
    <p>Hi! I’m Maren. I’ve been a single, working mom since my twins Theo and Ivy were the age of 5 and when my oldest daughter Nora had just turned 15. We lived in a great apartment on the upper eastside of Manhattan, right across from a park—it was a wonderful place to raise kids.</p>
    <p style="margin-top:24px">I was a Principal and the Chief Marketing Officer at a professional service firm for many years in midtown Manhattan. My undergraduate degree is in mathematics, and I have an MBA in marketing.</p>
    <p style="margin-top:24px">I love playing cards and all sorts of games—anything involving strategy. I love dancing—hip hop, in particular (not that I’m very good)—the music, beat, and the mind exercise in retaining the choreography is a complete enjoyable workout for me. Beyond this, I love exploring and learning new things, adventure, travel, philosophy, quantum theory and spirituality, to name just a few.</p>
  </div>
  <div class="btn" style="left:628px;top:1294px;width:142px;height:37px">Learn More</div>
</section>

<section class="crime">
  <div class="abs" style="left:70px;top:1499px;width:585px;height:380px;background:var(--panel)"></div>
  <div class="photo" style="left:135px;top:1546px;width:140px;height:139px;background:linear-gradient(#c9cdd0,#7b8a98)" role="img" aria-label="Misty pier"></div>
  <div class="photo" style="left:282px;top:1546px;width:139px;height:139px;background:linear-gradient(#8fb4d6,#6f8f3e)" role="img" aria-label="Barn in a field"></div>
  <div class="photo" style="left:135px;top:1693px;width:140px;height:139px;background:linear-gradient(#6b4a38,#b99579)" role="img" aria-label="Forest trunks"></div>
  <div class="photo" style="left:282px;top:1693px;width:139px;height:139px;background:linear-gradient(#2f4a35,#4e6a3c)" role="img" aria-label="Pine forest"></div>
  <div class="photo" style="left:429px;top:1693px;width:139px;height:139px;background:linear-gradient(#9ec2df,#2f6c9e)" role="img" aria-label="Person in a lake"></div>
  <div class="photo" style="left:628px;top:1431px;width:502px;height:331px;background:linear-gradient(160deg,#5b6470,#2c3036 60%,#6e7478)" role="img" aria-label="Police officers on a city street"></div>
  <h2 class="section-title" style="left:673px;top:1790px">Crime</h2>
  <p class="abs body-copy" style="left:673px;top:1863px;width:457px">The Mediterranean is everywhere--the view from our home or going down any street. Flowers of every color burst in odd places. There’s a stillness where you hear the birds chirping punctuated by the bleat of of pig. Paphos, which is on the western side of the island, has some of the most stunning sunsets in all the world.</p>
</section>

<section class="history">
  <div class="abs" style="left:70px;top:2082px;width:1060px;height:301px;background:var(--panel)"></div>
  <div class="photo" style="left:124px;top:2033px;width:307px;height:350px;background:linear-gradient(180deg,#3d7fc2 0%,#8ab1d6 30%,#9a5b3a 55%,#6a3b25 100%)" role="img" aria-label="Carved ancient stone temple"></div>
  <h2 class="section-title" style="left:468px;top:2118px">History</h2>
  <div class="abs" style="left:1060px;top:2128px;display:flex;gap:12px;align-items:center;color:#555;font-size:14px"><span>‹</span><span style="width:1px;height:18px;background:#555"></span><span>›</span></div>
  <p class="abs body-copy" style="left:468px;top:2181px;width:640px">The Mediterranean is everywhere--the view from our home or going down any street. Flowers of every color burst in odd places. There’s a stillness where you hear the birds chirping punctuated by the bleat of of pig. Paphos, which is on the western side of the island, has some of the most stunning sunsets in all the world.</p>
  <div class="btn" style="left:468px;top:2310px;width:142px;height:37px">Learn More</div>
</section>

<section class="crime-history">
  <h2 class="section-title center" style="top:2448px">Crime and History</h2>
  <div class="abs" style="left:66px;top:2596px;font-size:20px;color:#444">‹</div>
  <div class="abs" style="left:1122px;top:2596px;font-size:20px;color:#444">›</div>
  <div class="card" style="left:107px;top:2532px;width:297px;height:218px">
    <div class="photo" style="left:0;top:0;width:297px;height:154px;background:linear-gradient(135deg,#1c2a44,#2e4f7a)" role="img" aria-label="Hooded person at a laptop"></div>
    <div class="cap" style="top:176px">The Minoan Civilization</div>
  </div>
  <div class="card" style="left:451px;top:2532px;width:296px;height:218px">
    <div class="photo" style="left:0;top:0;width:296px;height:154px;background:linear-gradient(180deg,#5e8fc4,#c7a76e 60%,#8a7a66)" role="img" aria-label="Ancient hilltop ruins over a city"></div>
    <div class="cap" style="top:176px">A City Of Culture and Freedom</div>
  </div>
  <div class="card" style="left:794px;top:2532px;width:297px;height:218px">
    <div class="photo" style="left:0;top:0;width:297px;height:154px;background:linear-gradient(180deg,#d9b37c,#a8784a)" role="img" aria-label="Roman columns and ruins"></div>
    <div class="cap" style="top:176px">Romantic and Picturesque</div>
  </div>
</section>

<section class="travels">
  <h2 class="section-title center" style="top:2815px">Travels</h2>
  <div class="travel-card" style="left:70px;top:2936px;width:300px;height:471px;opacity:.4">
    <div class="photo" style="left:0;top:0;width:300px;height:310px;background:linear-gradient(#8d9a8c,#bfc7bd)" role="img" aria-label="Forest scene"></div>
    <div class="t-title" style="top:330px">Amsterdam, A City Of Culture</div>
    <div class="t-text" style="top:356px;font-size:11px;line-height:22px">We had a whirlwind 3 days in Amsterdam. We wanted to go to the canals first...</div>
    <div class="meta"></div>
  </div>
  <div class="travel-card" style="left:830px;top:2936px;width:300px;height:471px;opacity:.4">
    <div class="photo" style="left:0;top:0;width:300px;height:310px;background:linear-gradient(#8d9a8c,#bfc7bd)" role="img" aria-label="Forest scene"></div>
    <div class="t-title" style="top:330px">A City Of Culture and Freedom</div>
    <div class="t-text" style="top:356px;font-size:11px;line-height:22px">We spent every minute taking in the culture, and the day before I went online...</div>
    <div class="meta"><span style="position:absolute;right:14px;top:12px;font-size:10px">2 COMMENTS</span></div>
  </div>
  <div class="travel-card" style="left:278px;top:2910px;width:644px;height:534px;box-shadow:0 8px 30px rgba(0,0,0,.18)">
    <div class="photo" style="left:0;top:0;width:644px;height:350px;background:linear-gradient(180deg,#2f3e30,#5d6a4f 60%,#6c5a46)" role="img" aria-label="Woman in a hat facing a pine forest"></div>
    <div class="t-title" style="top:375px">Amsterdam, A City Of Culture and Freedom</div>
    <div class="t-text" style="top:404px">We had a whirlwind 3 days in Amsterdam, where we spent every minute taking in the culture. We wanted to go to the Canal Lantern House, so the day before I went online...</div>
    <div class="abs" style="left:0;top:460px;width:644px;text-align:center;font-size:13px;text-decoration:underline">Learn More</div>
    <div class="meta"><div style="position:absolute;left:22px;top:13px;display:flex;gap:18px"><span class="dot"></span><span class="dot"></span><span class="dot"></span><span class="dot"></span></div><span style="position:absolute;right:18px;top:11px">2 COMMENTS</span></div>
  </div>
  <svg class="abs" style="left:545px;top:3497px" width="20" height="30"><path d="M16 2L4 15l12 13" fill="none" stroke="#333" stroke-width="2"/></svg>
  <svg class="abs" style="left:635px;top:3497px" width="20" height="30"><path d="M4 2l12 13L4 28" fill="none" stroke="#333" stroke-width="2"/></svg>
</section>

<section class="food">
  <svg class="abs" style="left:68px;top:3621px" width="526" height="350" role="img" aria-label="Table spread with shared dishes and salads"><defs><linearGradient id="fg" x1="0" y1="0" x2="1" y2="1"><stop offset="0" stop-color="#d7c6a6"/><stop offset=".5" stop-color="#8a4a24"/><stop offset="1" stop-color="#3a2a1e"/></linearGradient></defs><polygon points="0,0 526,0 478,350 0,350" fill="url(#fg)"/></svg>
  <h2 class="section-title" style="left:634px;top:3707px">Food</h2>
  <p class="abs body-copy" style="left:634px;top:3777px;width:496px;text-align:left">The Mediterranean is everywhere--the view from our home or going down any street. Flowers of every color burst in odd places. There’s a stillness where you hear the birds chirping punctuated by the bleat of of pig. Paphos, which is on the western side of the island, has some of the most stunning sunsets in all the world.</p>
  <div class="btn" style="left:634px;top:3899px;width:142px;height:37px">Learn More</div>
  <div class="abs" style="left:1044px;top:3970px;width:22px;height:2px;background:#333"></div>
  <div class="abs" style="left:1076px;top:3970px;width:22px;height:2px;background:#ccc"></div>
  <div class="abs" style="left:1108px;top:3970px;width:22px;height:2px;background:#ccc"></div>
</section>

<section>
  <h2 class="section-title center" style="top:4036px">Guest Post</h2>
  <article class="abs guest" style="left:70px;top:4119px;width:316px">
    <div style="height:157px;background:linear-gradient(180deg,#8fb8e0,#4f9fc0 55%,#c8b28a)" role="img" aria-label="Woman looking at a beach"></div>
    <h3>The Minoan Civilization</h3><p>Many people have taken the leap from all walks of life and lifestyles.</p><div class="date">Mar 10, 2018</div>
  </article>
  <article class="abs guest" style="left:442px;top:4119px;width:315px">
    <div style="height:157px;background:linear-gradient(135deg,#c9c2b0,#7c8a5a)" role="img" aria-label="Two women laughing at a cafe"></div>
    <h3>The Minoan Civilization</h3><p>Many people have taken the leap from all walks of life and lifestyles.</p><div class="date">Mar 10, 2018</div>
  </article>
  <article class="abs guest" style="left:814px;top:4119px;width:316px">
    <div style="height:157px;background:linear-gradient(135deg,#d8d4cc,#5a4a3c)" role="img" aria-label="Plated gourmet dish"></div>
    <h3>The Minoan Civilization</h3><p>Many people have taken the leap from all walks of life and lifestyles.</p><div class="date">Mar 10, 2018</div>
  </article>
</section>

<section class="subscribe">
  <div class="abs" style="left:70px;top:4505px;font-size:11px;letter-spacing:1px;color:#555">SUBSCRIBE FOR UPDATES</div>
  <div class="abs" style="left:295px;top:4496px;width:320px;height:36px;border:1px solid var(--line);font-size:11px;color:#bbb;padding:10px 10px">Email Sign Up</div>
  <div class="abs" style="left:624px;top:4496px;width:157px;height:36px;background:var(--accent);color:#fff;font-size:12px;font-weight:500;display:flex;align-items:center;justify-content:center;letter-spacing:1px">SIGN UP</div>
  <div class="abs" style="left:850px;top:4505px;font-size:11px;letter-spacing:1px;color:#555">FOLLOW US</div>
  <div class="abs" style="left:962px;top:4508px;display:flex;gap:26px">
    <span class="dot" style="background:#555"></span><span class="dot" style="background:#555"></span><span class="dot" style="background:#555"></span><span class="dot" style="background:#555"></span><span class="dot" style="background:#555"></span>
  </div>
</section>

<footer class="abs footer">
  <div class="serif" style="position:absolute;left:0;width:1200px;top:56px;font-size:40px">The Pendry Parlour</div>
  <nav style="position:absolute;left:0;width:1200px;top:156px;display:flex;justify-content:center;gap:38px;font-size:12px;color:#aaa"><span>Home</span><span>About</span><span>Contact Us</span></nav>
  <div style="position:absolute;left:0;width:1200px;top:208px;font-size:10px;color:#888">© 2025 pendryparlour. &nbsp;All Rights Reserved.</div>
</footer>

</body>
</html>
```